Design for a Service-Based Estimate

We want a design for an Estimate that will always be sent in PDF format. The estimate or proposal is a critical document that needs to plainly show the service items, item description but also needs to be attractive and professional looking. Our current estimate deliverable is attached but it looks really basic like a Word document

```html
<!DOCTYPE html>
<html lang="en">
<head>
<meta charset="utf-8">
<title>Firmbase Paving Estimate</title>
<link rel="stylesheet" href="https://fonts.googleapis.com/css2?family=Poppins:wght@300;400;500;600;700;800&display=swap">
<style>
  :root {
    --navy: #302d55;
    --orange: #d5452a;
    --stone: #968d86;
    --ink: #2b2a3f;
    --muted: #a09ea8;
    --rule: #cfcdd4;
    --paper: #ffffff;
    --backdrop: #3a3d42;
  }
  * { margin: 0; padding: 0; box-sizing: border-box; }
  html, body { width: 838px; height: 1200px; overflow: hidden; }
  body {
    background: var(--backdrop);
    font-family: "Poppins", sans-serif;
    color: var(--ink);
    position: relative;
  }
  .page {
    position: absolute;
    left: 204px;
    width: 430px;
    height: 556px;
    background: var(--paper);
    overflow: hidden;
  }
  .page--invoice { top: 30px; }
  .page--terms { top: 614px; }

  /* Invoice page */
  .navy-block { position: absolute; left: 0; top: 0; width: 74px; height: 190px; background: var(--navy); }
  .brand-tab { position: absolute; left: 0; top: 22px; width: 200px; height: 34px; background: var(--paper); }
  .brand-name {
    position: absolute; left: 14px; top: 26px;
    font-weight: 800; font-size: 17px; letter-spacing: 0.5px;
    color: var(--navy); text-transform: uppercase;
  }
  .bill-to { position: absolute; left: 96px; top: 78px; }
  .bill-to__label { color: var(--orange); font-weight: 700; font-size: 11px; }
  .bill-to__name { color: var(--muted); font-weight: 300; font-size: 18px; line-height: 1.2; }
  .bill-to__line { font-weight: 600; font-size: 8.5px; line-height: 1.5; color: var(--ink); }
  .doc-title {
    position: absolute; right: 24px; top: 70px;
    font-size: 34px; font-weight: 300; color: var(--navy); letter-spacing: 1px;
  }
  .doc-title strong { font-weight: 800; }
  .project {
    position: absolute; right: 24px; top: 160px; width: 220px;
    border-top: 1px solid var(--muted); padding-top: 8px;
    text-align: right; color: var(--muted); font-size: 10px; line-height: 1.4;
  }
  .line-items { position: absolute; left: 22px; top: 226px; width: 386px; border-collapse: collapse; }
  .line-items th {
    background: var(--orange); color: var(--paper);
    font-size: 8.5px; font-weight: 600; padding: 6px 4px; text-align: center;
  }
  .line-items th:first-child { border-radius: 12px 0 0 12px; }
  .line-items th:last-child { border-radius: 0 12px 12px 0; }
  .line-items td {
    font-size: 7px; padding: 8px 5px; vertical-align: top; text-align: center;
    border-left: 1px solid var(--rule); border-bottom: 1px solid var(--rule);
  }
  .line-items td:first-child { border-left: none; text-align: left; width: 44%; }
  .line-items .desc-sm { font-size: 5.5px; line-height: 1.5; }
  .line-items .spacer td { height: 52px; border-bottom: none; }
  .line-items .total td { border-bottom: none; color: var(--orange); font-weight: 700; }
  .watermark {
    position: absolute; left: 24px; top: 410px;
    font-weight: 800; font-size: 34px; color: #ebeaee; text-transform: uppercase; letter-spacing: 1px;
  }
  .band-stone { position: absolute; left: 0; bottom: 48px; width: 150px; height: 20px; background: var(--stone); }
  .block-orange { position: absolute; right: 0; bottom: 0; width: 150px; height: 62px; background: var(--orange); }

  /* Terms page */
  .page--terms .brand-name { left: 26px; top: 26px; }
  .terms-pill {
    position: absolute; left: 50%; top: 66px; transform: translateX(-50%);
    background: var(--navy); color: var(--paper); font-weight: 700; font-size: 13px;
    padding: 4px 18px; border-radius: 14px;
  }
  .navy-square { position: absolute; right: 0; top: 112px; width: 32px; height: 48px; background: var(--navy); }
  .terms-text { position: absolute; left: 26px; top: 112px; width: 352px; font-size: 7px; line-height: 1.55; }
  .terms-text p { margin-bottom: 1px; }
  .sign-line { position: absolute; border-top: 1px solid var(--ink); width: 150px; }
  .sign-label { position: absolute; font-size: 8px; font-weight: 600; color: var(--navy); }
  .terms-orange { position: absolute; left: 0; top: 408px; width: 96px; height: 62px; background: var(--orange); }
  .terms-stone { position: absolute; right: 44px; bottom: 0; width: 72px; height: 62px; background: var(--stone); }
</style>
</head>
<body>

<section class="page page--invoice">
  <div class="navy-block"></div>
  <div class="brand-tab"></div>
  <div class="brand-name">Firmbase Paving</div>

  <div class="bill-to">
    <div class="bill-to__label">Invoice To:</div>
    <div class="bill-to__name">Dana Whitfield</div>
    <div class="bill-to__line">742 Harbor Lane Se Fairview 34990</div>
    <div class="bill-to__line">dwhitfield@example.com</div>
  </div>

  <div class="doc-title"><strong>IN</strong>VOICE</div>

  <div class="project">
    Dana Whitfield New Concrete Pad<br>
    742 Harbor Lane Se Fairview 34990<br>
    Bid#:20-0182
  </div>

  <table class="line-items">
    <thead>
      <tr><th>Item</th><th>Quantity</th><th>U/M</th><th>Unit $</th><th>Total $</th></tr>
    </thead>
    <tbody>
      <tr>
        <td class="desc-sm">Form, Pour &amp; Finish New Concrete Slab (24' x 24' x 4") Includes 3000psi Concrete Mix, Footer (12" x 8") with One (#5) Continuous Rebar, Wire Mesh Reinforcement and Saw-Cut Expansion Joints</td>
        <td>576</td><td>SF</td><td>$8.65</td><td>$4,982.40</td>
      </tr>
      <tr>
        <td>OPTIONAL: Add (2' x 24' x 4") Small Ramp Area</td>
        <td>48</td><td>SF</td><td>$8.65</td><td>$415.20</td>
      </tr>
      <tr class="spacer"><td></td><td></td><td></td><td></td><td></td></tr>
      <tr class="total"><td></td><td></td><td></td><td>Total Price</td><td>$5,397.60</td></tr>
    </tbody>
  </table>

  <div class="watermark" aria-hidden="true">Firmbase Paving</div>
  <div class="band-stone"></div>
  <div class="block-orange"></div>
</section>

<section class="page page--terms">
  <div class="brand-name">Firmbase Paving</div>
  <div class="terms-pill">Terms and Condition</div>
  <div class="navy-square"></div>

  <div class="terms-text">
    <p>Price as quoted in this estimate are valid for (60) days only.</p>
    <p>Payment in full, less any previously paid amounts, is due to the Contractor upon completion of the proposed scope of work.</p>
    <p>All change order requests must be communicated in writing to the Contractor by the Client or their authorized representative.</p>
    <p>All measurements listed in this estimate are approximate and may vary slightly due to actual field conditions.</p>
    <p>It is agreed by the Contractor and the Client that complications and costs arising from unforeseen conditions and handling of unsuitable materials are not included in this estimate.</p>
    <p>Unless specifically listed in this estimate the following items and their costs are not included: Maintenance of Traffic, Concrete Material Pumping, Testing, Excavation, Grading and Fill Material, Permits and Fees, Surveying and AS-Builts, Irrigation Repair, Landscaping and Root Mitigation, De-watering, Private Locates and Accessibility.</p>
    <p>Private utility locating services using radio detection devices and, when necessary, ground penetrating radar are offered by Firmbase Paving to assist in finding private utilities that may not have been located by the public one call system. Firmbase Paving will not be responsible for private utilities that have not been located nor for the failure of the above equipment to accurately detect existing utilities since the equipment is fallible and existing site conditions may preclude the ability of the equipment to detect an identifiable signal.</p>
  </div>

  <div class="sign-label" style="left:40px; top:372px;">Client Signature</div>
  <div class="sign-line" style="left:40px; top:386px;"></div>
  <div class="sign-label" style="left:240px; top:436px;">Date</div>
  <div class="sign-line" style="left:240px; top:450px;"></div>

  <div class="terms-orange"></div>
  <div class="terms-stone"></div>
</section>

</body>
</html>
```